2024 Harwick Patrol Deputy's Statute Handbook

Cover, spine and back cover for our annual Statute Handbook. The overall size of the cover is 18.82 x 11 (with the .25 inch bleed it is 19.32 x 11.5) and the spine is 1.82 x 11 plus (1.82 x 11.5 with the bleed).
The book comes with a motor vehicle companion guide which will be 5" X 7" with spiral binding. The companion guide will have the same design with a slight twist related to motor vehicle law.

```html
<!DOCTYPE html>
<html lang="en">
<head>
<meta charset="utf-8">
<title>Harwick Patrol Deputy's Statute Handbook 2024</title>
<link rel="stylesheet" href="https://fonts.googleapis.com/css2?family=Russo+One&family=Oswald:wght@400;600;700&family=Poppins:wght@400&display=swap">
<style>
  :root {
    --stage: #e9eaec;
    --night: #0e1420;
    --steel: #1d2838;
    --slate: #34404f;
    --teal: #1fb3b0;
    --gold: #c99a2e;
    --gold-light: #e7c25c;
    --silver: #c9ccd1;
    --white: #ffffff;
    --flag-red: #8a2a30;
    --flag-blue: #1b2846;
    --hazard: #b89a1e;
  }
  * { margin: 0; padding: 0; box-sizing: border-box; }
  html, body { width: 1200px; height: 668px; overflow: hidden; }
  body { background: var(--stage); position: relative; font-family: "Poppins", sans-serif; }

  .book-wrap { position: absolute; left: 26px; top: 94px; width: 821px; height: 480px; display: flex; }
  .back-cover, .spine, .front-cover { position: relative; height: 480px; overflow: hidden; background: var(--night); }
  .back-cover { width: 371px; }
  .spine { width: 79px; border-left: 1px solid #000; border-right: 1px solid #000; }
  .front-cover { width: 371px; }

  .photo-fill { position: absolute; inset: 0; }
  .back-cover .photo-fill { background: linear-gradient(160deg, #2b3646 0%, #161d29 45%, #0b1018 100%); }
  .front-cover .photo-fill { background: linear-gradient(170deg, #1a2230 0%, #24364a 35%, #121a26 70%, #0a0e15 100%); }
  .spine .photo-fill { background: linear-gradient(180deg, #1e2838 0%, #111823 60%, #0b0f16 100%); }

  .title-small, .title-big, .title-year { font-family: "Russo One", sans-serif; text-transform: uppercase; text-align: center; line-height: 0.95; }
  .title-small { color: var(--teal); }
  .title-big { color: var(--gold-light); }
  .title-year { color: var(--teal); letter-spacing: 0.35em; }

  /* back */
  .back-title { position: absolute; top: 22px; left: 0; right: 0; }
  .back-title .title-small { font-size: 19px; }
  .back-title .title-big { font-size: 30px; }
  .back-title .title-year { font-size: 16px; margin-top: 2px; }
  .back-copy { position: absolute; top: 118px; left: 16px; right: 16px; color: var(--white); font-size: 7.6px; line-height: 1.45; text-align: justify; }
  .back-copy p + p { margin-top: 9px; }

  /* spine */
  .spine-badge { position: absolute; top: 14px; left: 50%; transform: translateX(-50%); width: 22px; height: 22px; border-radius: 50%; background: var(--gold); }
  .spine-title { position: absolute; left: 50%; top: 48px; width: 250px; transform-origin: 0 0; transform: rotate(90deg) translateY(-50%); display: flex; flex-direction: column; align-items: center; gap: 3px; white-space: nowrap; }
  .spine-title .spine-line { display: flex; align-items: baseline; gap: 8px; }
  .spine-title .title-small { font-size: 11px; }
  .spine-title .title-big { font-size: 20px; }
  .spine-title .title-year { font-size: 11px; letter-spacing: 0.15em; }
  .spine-author { position: absolute; bottom: 16px; left: 50%; width: 140px; transform-origin: 0 0; transform: rotate(90deg) translate(-100%, -50%); font-family: "Oswald", sans-serif; font-size: 9px; color: var(--white); letter-spacing: 0.06em; text-align: center; text-transform: uppercase; white-space: nowrap; }

  /* front */
  .author { font-family: "Oswald", sans-serif; font-weight: 600; color: var(--white); letter-spacing: 0.06em; text-transform: uppercase; text-align: center; }
  .front-cover .author { position: absolute; top: 20px; left: 0; right: 0; font-size: 16px; }
  .front-title { position: absolute; top: 50px; left: 0; right: 0; }
  .front-title .title-small { font-size: 22px; }
  .front-title .title-big { font-size: 50px; margin-top: 2px; }
  .front-title .title-year { font-size: 34px; margin-top: 4px; }
  .cuffs-area { position: absolute; left: 10px; top: 262px; width: 170px; height: 190px; background: radial-gradient(ellipse at 45% 50%, rgba(205,209,215,0.45) 0%, rgba(130,138,150,0.25) 40%, rgba(20,26,36,0) 70%); }
  .firm-mark { position: absolute; display: flex; align-items: center; gap: 5px; font-family: "Oswald", sans-serif; font-weight: 600; color: var(--gold-light); text-transform: uppercase; letter-spacing: 0.05em; }
  .firm-mark .dot { border-radius: 50%; background: var(--gold); }
  .front-cover .firm-mark { left: 188px; top: 312px; font-size: 12px; }
  .front-cover .firm-mark .dot { width: 30px; height: 30px; }
  .flag-band { position: absolute; left: 0; right: 0; bottom: 0; height: 120px; background: linear-gradient(165deg, rgba(27,40,70,0) 0%, var(--flag-blue) 35%, var(--flag-red) 75%, #5a1c22 100%); }
  .state-block { position: absolute; left: 0; right: 0; text-align: center; color: var(--white); }
  .front-cover .state-block { top: 396px; }
  .state-name { font-family: "Oswald", sans-serif; font-weight: 700; font-size: 26px; line-height: 1; text-transform: uppercase; letter-spacing: 0.02em; }
  .state-sub { font-family: "Oswald", sans-serif; font-size: 14px; line-height: 1.1; text-transform: uppercase; }
  .topics { margin-top: 4px; font-family: "Oswald", sans-serif; font-size: 9px; text-transform: uppercase; letter-spacing: 0.02em; }
  .topics .sep { color: var(--gold-light); margin: 0 3px; }

  /* companion guide */
  .guide { position: absolute; left: 887px; top: 134px; width: 286px; height: 400px; overflow: hidden; background: var(--night); }
  .hazard-band { position: absolute; left: 0; right: 0; top: 0; height: 70px; background: linear-gradient(180deg, #2f2a12 0%, #4a3f14 50%, rgba(20,24,32,0) 100%); }
  .guide-photo { position: absolute; left: 0; right: 0; top: 150px; height: 180px; background: linear-gradient(100deg, #2b3a2e 0%, #3a4a52 40%, #6f7a86 70%, #1e2632 100%); }
  .guide .flag-band { height: 90px; }
  .guide-title { position: absolute; top: 40px; left: 0; right: 0; }
  .guide-title .title-small { font-size: 14px; }
  .guide-title .title-big { font-size: 30px; }
  .guide-title .title-silver { font-family: "Russo One", sans-serif; color: var(--silver); font-size: 36px; text-transform: uppercase; text-align: center; line-height: 0.95; }
  .guide-title .title-year { font-size: 20px; letter-spacing: 0.1em; margin-top: 2px; }
  .guide .firm-mark { left: 50%; transform: translateX(-50%); top: 236px; font-size: 10px; }
  .guide .firm-mark .dot { width: 24px; height: 24px; }
  .guide .state-block { top: 312px; }
  .guide .state-name { font-size: 22px; }
  .guide .state-sub { font-size: 12px; }
  .guide-rules { font-family: "Oswald", sans-serif; font-size: 9px; color: var(--gold-light); text-transform: uppercase; }
  .guide .author { position: absolute; bottom: 14px; left: 0; right: 0; font-size: 11px; }
</style>
</head>
<body>
  <div class="book-wrap">
    <section class="back-cover">
      <div class="photo-fill" role="img" aria-label="Dark photograph of a uniformed officer's torso and duty belt"></div>
      <div class="back-title">
        <div class="title-small">Patrol Deputy's</div>
        <div class="title-big">Statute Handbook</div>
        <div class="title-year">2024</div>
      </div>
      <div class="back-copy">
        <p>This handbook gathers the statutes, procedures and case guidance that patrol deputies rely on every shift. Each chapter is written in plain language, organized for quick reference, and updated for the current year so officers can act with confidence in the field.</p>
        <p>Inside you will find arrest and search rules, elements of common offenses, juvenile procedures and motor vehicle enforcement, each supported by clear examples and citations. Tables and checklists make it easy to confirm the right step before writing a report or appearing in court.</p>
        <p>Written by a practicing attorney and former instructor, the 2024 edition reflects recent legislative changes and appellate decisions. Keep it in your cruiser, your locker or your training room as a trusted companion throughout the year.</p>
      </div>
    </section>

    <section class="spine">
      <div class="photo-fill" role="img" aria-label="Dark textured police background"></div>
      <div class="spine-badge"></div>
      <div class="spine-title">
        <div class="spine-line">
          <span class="title-small">Patrol Deputy's</span>
          <span class="title-year">2024</span>
        </div>
        <span class="title-big">Statute Handbook</span>
      </div>
      <div class="spine-author">Daniel R. Whitcombe Esq.</div>
    </section>

    <section class="front-cover">
      <div class="photo-fill" role="img" aria-label="Dark photograph of a police vest and patrol lettering"></div>
      <div class="flag-band" role="img" aria-label="Waving flag with stars and stripes"></div>
      <div class="cuffs-area" role="img" aria-label="Photograph of steel handcuffs"></div>
      <div class="author">Daniel R. Whitcombe Esq.</div>
      <div class="front-title">
        <div class="title-small">Patrol Deputy's</div>
        <div class="title-big">Statute<br>Handbook</div>
        <div class="title-year">2024</div>
      </div>
      <div class="firm-mark"><span class="dot"></span>Whitcombe</div>
      <div class="state-block">
        <div class="state-name">Harwick</div>
        <div class="state-sub">Patrol Deputy's<br>Guide to</div>
        <div class="topics">Criminal Procedure<span class="sep">•</span>Statutory Law<span class="sep">•</span>Motor Vehicle Law<span class="sep">•</span>Juvenile Law</div>
      </div>
    </section>
  </div>

  <section class="guide">
    <div class="hazard-band" role="img" aria-label="Yellow and black hazard stripes"></div>
    <div class="guide-photo" role="img" aria-label="Photograph of officers in high-visibility vests beside a patrol car"></div>
    <div class="flag-band" role="img" aria-label="Waving flag with stars and stripes"></div>
    <div class="guide-title">
      <div class="title-small">Patrol Deputy's</div>
      <div class="title-big">Motor Vehicle</div>
      <div class="title-silver">Guide</div>
      <div class="title-year">2024</div>
    </div>
    <div class="firm-mark"><span class="dot"></span>Whitcombe</div>
    <div class="state-block">
      <div class="state-name">Harwick</div>
      <div class="state-sub">Patrol Deputy's</div>
      <div class="guide-rules">Motor Vehicle Guide and Rules</div>
    </div>
    <div class="author">Daniel R. Whitcombe Esq.</div>
  </section>
</body>
</html>
```